Need a fun and informative infographic!

We need an infographic to describe our "client experience" which consists of 4 phases - see info about each of our "phases" which includes our available suite of services. UPDATED THE TEXT IN A NEW FILE CALLED "Client Experience Infographic Info".

We intend to use the infographic in both print and digital in a printed "leave behind", in packets for new clients, and possible on the website.

Keystone Tutorial www.keystonetutorial.example

Target Market(s)

Families of children aged Kindergarten through 12th Grade; affluent communities who have expendable income to spend on private tutoring and test prep.

Industry/Entity Type

Education

Font styles to use
Sans Serif

Requirements
Must have
• My project must use our brand colors.
• Light Blue CMYK: 60 27 0 0 RGB: 115 165 215
• Dark Blue CMYK: 93 85 36 27 RGB: 43 57 94
• Orange CMYK: 0 46 77 10 RGB: 230 125 53

```html
<!DOCTYPE html>
<html lang="en">
<head>
<meta charset="utf-8">
<title>The Client Experience – Keystone Tutorial</title>
<link rel="stylesheet" href="https://fonts.googleapis.com/css2?family=Fredoka:wght@600;700&family=Open+Sans:wght@400;600;700&display=swap">
<style>
  :root {
    --orange: #e67d35;
    --light-blue: #73a5d7;
    --pale-blue: #c9dbee;
    --dark-blue: #2b395e;
    --white: #ffffff;
    --number-grey: #8fa6c2;
  }
  * { box-sizing: border-box; margin: 0; padding: 0; }
  html, body { width: 788px; height: 1200px; overflow: hidden; }
  body {
    position: relative;
    background: var(--orange);
    font-family: "Open Sans", Arial, sans-serif;
    color: var(--dark-blue);
  }
  .masthead { position: absolute; top: 0; left: 0; width: 788px; height: 168px; text-align: center; }
  .masthead-title {
    margin-top: 16px;
    font-family: "Fredoka", "Arial Rounded MT Bold", sans-serif;
    font-weight: 700;
    font-size: 50px;
    line-height: 1;
    letter-spacing: 1px;
    color: var(--light-blue);
    -webkit-text-stroke: 2px var(--dark-blue);
  }
  .brand-name {
    margin-top: 22px;
    font-weight: 700;
    font-size: 32px;
    color: var(--white);
  }
  .phase { position: absolute; left: 0; width: 788px; }
  .phase-panel { position: absolute; inset: 0; background: var(--light-blue); }
  .phase-one { top: 168px; height: 250px; }
  .phase-one .phase-panel { clip-path: polygon(0 0, 84% 0, 77% 100%, 0 100%); }
  .phase-two { top: 432px; height: 240px; }
  .phase-two .phase-panel { clip-path: polygon(22% 0, 100% 0, 100% 100%, 15% 100%); }
  .phase-three { top: 686px; height: 232px; }
  .phase-three .phase-panel { clip-path: polygon(0 0, 79% 0, 86% 100%, 0 100%); }
  .phase-four { top: 932px; height: 268px; }
  .phase-four .phase-panel { clip-path: polygon(20% 0, 100% 0, 100% 100%, 26% 100%); }

  .phase-heading {
    position: absolute;
    top: 10px;
    background: var(--pale-blue);
    text-align: center;
    padding: 6px 12px;
  }
  .phase-label { font-size: 14px; font-weight: 600; }
  .phase-name { font-size: 24px; font-weight: 700; line-height: 1.15; }

  .phase-number {
    position: absolute;
    width: 136px; height: 136px;
    border-radius: 50%;
    background: var(--white);
    border: 5px solid var(--dark-blue);
    font-family: "Fredoka", sans-serif;
    font-weight: 700;
    font-size: 96px;
    line-height: 124px;
    text-align: center;
    color: var(--number-grey);
  }
  .illustration { position: absolute; border-radius: 6px; }
  .points { position: absolute; list-style: none; font-size: 10.5px; line-height: 1.45; }
  .points li { position: relative; padding-left: 10px; }
  .points li::before {
    content: ""; position: absolute; left: 0; top: 6px;
    width: 4px; height: 4px; border-radius: 50%; background: var(--dark-blue);
  }
</style>
</head>
<body>

<header class="masthead">
  <h1 class="masthead-title">THE CLIENT EXPERIENCE</h1>
  <div class="brand-name">Keystone Tutorial</div>
</header>

<section class="phase phase-one">
  <div class="phase-panel"></div>
  <div class="phase-heading" style="left:220px; width:340px;">
    <div class="phase-label">Phase 1</div>
    <h2 class="phase-name">The Consultation</h2>
  </div>
  <ul class="points" style="left:30px; top:96px; width:150px;">
    <li>The process begins with a complimentary and thorough consultation.</li>
  </ul>
  <ul class="points" style="left:192px; top:96px; width:170px;">
    <li>One of our local Educational Directors meets in person (or via video call if necessary) with the parents and student to become acquainted and to better understand the family's needs.</li>
  </ul>
  <div class="illustration" role="img" aria-label="Three people in conversation with question and answer speech bubbles"
       style="left:380px; top:88px; width:200px; height:148px; background:linear-gradient(180deg, #dce7f3 0%, #b3cbe5 100%);"></div>
  <div class="phase-number" style="left:630px; top:57px;">1</div>
</section>

<section class="phase phase-two">
  <div class="phase-panel"></div>
  <div class="phase-heading" style="left:450px; width:320px;">
    <div class="phase-label">Phase 2</div>
    <h2 class="phase-name">Match and Customize</h2>
  </div>
  <div class="phase-number" style="left:22px; top:52px;">2</div>
  <div class="illustration" role="img" aria-label="Tutor beside a student profile document"
       style="left:196px; top:86px; width:130px; height:138px; background:linear-gradient(180deg, #f3f6fa 0%, #c9dbee 100%);"></div>
  <ul class="points" style="left:350px; top:94px; width:186px;">
    <li>Students are matched with a tutor or a team of tutors based on a careful understanding of each student's unique learning style, academic goals, personality, and schedule.</li>
  </ul>
  <ul class="points" style="left:556px; top:94px; width:214px;">
    <li>The tutor(s) develop a personalized curriculum that aligns with the student's existing strengths and areas for improvement, while addressing all factors impacting performance such as test anxiety and self-confidence.</li>
  </ul>
</section>

<section class="phase phase-three">
  <div class="phase-panel"></div>
  <div class="phase-heading" style="left:250px; width:300px;">
    <div class="phase-label">Phase 3</div>
    <h2 class="phase-name">Communication</h2>
  </div>
  <ul class="points" style="left:30px; top:94px; width:160px;">
    <li>Tutoring sessions occur in the home, our offices, remotely, or a location of the family's choosing; scheduling is based on the availability of the student.</li>
  </ul>
  <ul class="points" style="left:204px; top:94px; width:196px;">
    <li>Our custom built "Dashboard" allows parents and our Directors to access a thorough "session summary" after each session giving them a detailed review of the tutoring session and the student's homework for the coming week.</li>
  </ul>
  <div class="illustration" role="img" aria-label="Person beside an open laptop showing a session summary"
       style="left:420px; top:88px; width:180px; height:128px; background:linear-gradient(180deg, #f3f6fa 0%, #b3cbe5 100%);"></div>
  <div class="phase-number" style="left:640px; top:48px;">3</div>
</section>

<section class="phase phase-four">
  <div class="phase-panel"></div>
  <div class="phase-heading" style="left:430px; width:340px;">
    <div class="phase-label">Ongoing:</div>
    <h2 class="phase-name">Our Suite of Services</h2>
  </div>
  <div class="phase-number" style="left:26px; top:66px;">4</div>
  <div class="illustration" role="img" aria-label="Educational Director in a suit"
       style="left:196px; top:92px; width:110px; height:140px; background:linear-gradient(180deg, #dce7f3 0%, #9fbde0 100%);"></div>
  <ul class="points" style="left:318px; top:92px; width:142px;">
    <li>Our Educational Directors are communicative and responsive, ready to provide guidance and seamless coordination of whatever services the student requires.</li>
  </ul>
  <ul class="points" style="left:470px; top:92px; width:150px;">
    <li>No matter where along the path our relationship begins, we continue to support our students and families in a myriad of ways including:<br>- Standardized Test Prep<br>- Subject Tutoring<br>- College Admissions</li>
  </ul>
  <ul class="points" style="left:630px; top:92px; width:148px;">
    <li>When appropriate, we introduce Executive Function tutoring to help students improve their executive functioning, organizational and time management skills.</li>
  </ul>
</section>

</body>
</html>
```